update and create new Sorvane Dojo Karate Website

We require a new and modernised website for our Karate school.
Website currently is www.Sorvanedojo.example
Please check the current state of the website to start off with.
The basis of the brief attached is to provide context on what we want for the new website.

1) Please read through the build brief attached.
2) We are looking for a vendor who can service our organisation's website needs in future and ongoing.
3) Our budget is more than currently able to post on here and is subject to discussion should we choose you as our vendor. The amount initially is priced to be between $700.00 - $1000.00 AUD for the selected website.
4) easy and simple use and communication is a must.
5) this build request is subject to updating should we require further needs on the website.
6) The reason we have chosen the "refundable" option at this stage is because we've never used Pixel Forum before. However the winning vendor will receive full commission and continued pay ongoing for future management of the website.

Thank you
Milo
Updates

Hi Designers and Vendors Regarding this website. Our budget is set at approx. $1000.00 with ongoing work commission to run the website. I advise you read what is re

Industry/Entity Type

Communication

```html
<!DOCTYPE html>
<html lang="en">
<head>
<meta charset="utf-8">
<title>Sorvane Dojo Karate</title>
<link rel="stylesheet" href="https://fonts.googleapis.com/css2?family=Raleway:wght@400;500;600&family=Open+Sans:wght@400;600;700&display=swap">
<style>
:root{
  --red:#b0101c;
  --red-dark:#8a0a14;
  --red-mid:#c4121f;
  --yellow:#f2f20f;
  --text:#333;
  --muted:#666;
  --footer:#333333;
  --footer-bottom:#262626;
  --white:#fff;
}
*{margin:0;padding:0;box-sizing:border-box}
html,body{width:964px;height:1200px;overflow:hidden}
body{position:relative;background:var(--white);font-family:"Open Sans",sans-serif;color:var(--text)}
.top-band{position:absolute;left:0;top:0;width:964px;height:349px;background:linear-gradient(#fff 0,#ececec 100%)}
.brand{position:absolute;left:114px;top:44px;display:flex;align-items:center;gap:10px}
.brand-mark{width:34px;height:34px;border-radius:50%;background:var(--red)}
.brand-name{font-family:"Raleway",sans-serif;font-weight:600;font-size:22px;color:var(--red)}
.brand-url{position:absolute;left:158px;top:81px;font-size:10px;color:var(--muted)}
.nav{position:absolute;left:112px;top:110px;width:744px;height:37px;background:linear-gradient(#c8101e,#a00a16);display:flex;box-shadow:0 4px 14px rgba(0,0,0,.25)}
.nav a{font-family:"Raleway",sans-serif;font-weight:500;font-size:12.5px;color:var(--white);text-decoration:none;line-height:37px;padding:0 14px;border-right:1px solid rgba(0,0,0,.25)}
.nav a:first-child{padding-left:31px}
.nav a:last-child{border-right:0}
.hero{position:absolute;left:112px;top:147px;width:743px;height:309px;background:linear-gradient(100deg,#c9c4be 0%,#e9e6e1 40%,#f4f2ee 70%,#b5aaa0 100%);box-shadow:0 6px 18px rgba(0,0,0,.2)}
.hero-card{position:absolute;left:35px;top:92px;width:296px;height:117px;background:var(--yellow);padding:20px 12px 0 21px;overflow:hidden}
.hero-title{font-family:"Raleway",sans-serif;font-weight:500;font-size:27px;line-height:28px;color:var(--red);white-space:nowrap}
.hero-sub{font-family:"Raleway",sans-serif;font-size:14px;line-height:18px;color:#333;margin-top:1px;white-space:nowrap}
.hero-text{font-size:8px;line-height:14px;color:#555;margin-top:3px}
.dots{position:absolute;left:346px;top:285px;display:flex;gap:3px}
.dots span{width:10px;height:10px;border-radius:50%;background:#333}
.welcome{position:absolute;left:112px;top:484px;width:484px}
.welcome h1{font-family:"Raleway",sans-serif;font-weight:500;font-size:23px;color:#222;margin-bottom:10px}
.welcome p{font-size:8px;line-height:14px;color:#444;margin-bottom:6px;padding-left:1px}
.btn-yellow{display:inline-block;margin-top:6px;margin-left:2px;width:83px;height:24px;background:var(--yellow);border:1px solid #d8d800;font-size:8.5px;font-weight:700;line-height:22px;text-align:center;color:#222}
.promo{position:absolute;left:633px;top:480px;width:216px;height:190px;background:var(--red)}
.promo-photo{height:97px;background:linear-gradient(90deg,#8c8c8c,#d9d9d9 45%,#b7b3ae)}
.promo h2{font-family:"Raleway",sans-serif;font-weight:500;font-size:18px;color:var(--white);margin:8px 0 0 16px}
.promo p{font-size:8px;line-height:13px;color:#f2d4d6;margin:3px 14px 0 16px}
.btn-dark{display:block;margin:7px 0 0 17px;width:78px;height:19px;background:var(--red-dark);color:var(--white);font-size:8px;font-weight:600;line-height:19px;text-align:center;box-shadow:0 1px 2px rgba(0,0,0,.4)}
.divider{position:absolute;left:110px;top:708px;width:737px;height:1px;background:#d5d5d5}
.articles-title{position:absolute;left:110px;top:731px;font-family:"Raleway",sans-serif;font-weight:500;font-size:20px;color:var(--red)}
.article{position:absolute;width:360px;height:83px}
.article-photo{position:absolute;left:0;top:0;width:122px;height:83px}
.article h3{position:absolute;left:133px;top:-2px;font-family:"Raleway",sans-serif;font-weight:500;font-size:13.5px;color:#222}
.article p{position:absolute;left:133px;top:15px;width:225px;font-size:8px;line-height:14px;color:#666}
.article .more{position:absolute;left:133px;top:74px;font-size:8px;font-weight:600;color:var(--red)}
.footer{position:absolute;left:0;top:1013px;width:964px;height:146px;background:var(--footer)}
.footer-col{position:absolute;top:29px;list-style:none}
.footer-col li{font-family:"Raleway",sans-serif;font-size:10px;color:#eee;line-height:17.3px}
.footer-contact{position:absolute;left:393px;top:28px;color:#eee}
.footer-contact h4{font-family:"Raleway",sans-serif;font-weight:400;font-size:13px;margin-bottom:6px}
.footer-contact .addr{font-size:8px}
.footer-contact .phone{font-size:11px;margin-top:5px}
.footer-contact .mail{font-size:8px;margin-top:6px}
.footer-brand{position:absolute;left:598px;top:62px;display:flex;align-items:center;gap:8px}
.footer-brand .brand-mark{width:26px;height:26px}
.footer-brand .brand-name{font-size:17px;color:#e8e8e8}
.bottom-bar{position:absolute;left:0;top:1159px;width:964px;height:41px;background:var(--footer-bottom)}
.copyright{position:absolute;left:112px;top:15px;font-size:8px;color:#aaa}
</style>
</head>
<body>
<div class="top-band"></div>

<div class="brand"><span class="brand-mark"></span><span class="brand-name">Sorvane Dojo Karate</span></div>
<div class="brand-url">www.Sorvanedojo.example</div>

<nav class="nav">
  <a>Home</a><a>About Us</a><a>Location &amp; Times</a><a>News&nbsp; Events</a><a>Gallery &amp; Videos</a><a>Get Started</a><a>Contact Us</a>
</nav>

<section class="hero" role="img" aria-label="Photo of a karate student in a white gi breaking a wooden board">
  <div class="hero-card">
    <div class="hero-title">KARATE TRAINING</div>
    <div class="hero-sub">NULLAM ENIM LEO EGESTAS</div>
    <div class="hero-text">Mauris vel lacus vitae felis vestibulum volutpat Etiam est<br>nunc venenatis in tristique eu imperdiet ac nisl</div>
  </div>
  <div class="dots"><span></span><span></span><span></span><span></span></div>
</section>

<section class="welcome">
  <h1>Welcome to Sorvane Dojo Website</h1>
  <p>Welcome to Sorvane Dojo Karate, to our Dojo and to our events as we invite all Karate-ka and visitors world-wide to experience what we do and invite them to part-take in our Karate activities.</p>
  <p>The head of the organisation is Daniel Kerris, Kancho - Australia's most prominent Kempo instructor - one of Australia's leading Karate teachers. Sorvane Dojo is based in Sydney, Australia and is known as Australia's leading Kempo group. Whilst all our Dojo are all located in Sydney we have a broad-base support across the city and are very active in the Australian Karate (Martial Arts) community.</p>
  <p>Our style is a Japanese Kempo Style, whilst other styles of Kempo are American (Kenpo), or western freestyle based; we attempt to maintain the traditions and cultures of Japanese Karate in our teaching and Dojo culture.</p>
  <span class="btn-yellow">GET STARTED</span>
</section>

<aside class="promo">
  <div class="promo-photo" role="img" aria-label="Photo of a student kicking a red training pad in a dojo"></div>
  <h2>Try 2 free classes</h2>
  <p>Class aptent taciti sociosqu ad litora torquent per conubia nostra per inceptos hymec</p>
  <span class="btn-dark">GET STARTED</span>
</aside>

<div class="divider"></div>
<h2 class="articles-title">Karate Articles</h2>

<article class="article" style="left:110px;top:773px">
  <div class="article-photo" role="img" aria-label="Photo of a karateka performing a flying kick" style="background:linear-gradient(135deg,#e6e6e6,#bdbdbd)"></div>
  <h3>Warm Ups</h3>
  <p>Cum sociis natoque penatibus et magnis dis parturient montes nascetur ridiculus mus In iaculis facilisis massa Etiam eu urna Sed porta Suspendisse quam leo molestie sed luctus quis feugiat in pede Fusce</p>
  <span class="more">READ MORE</span>
</article>
<article class="article" style="left:505px;top:773px">
  <div class="article-photo" role="img" aria-label="Photo of students in white gi with belts practising kata" style="background:linear-gradient(135deg,#9a9a9a,#dcdcdc 50%,#7a7f8c)"></div>
  <h3>Kata Training</h3>
  <p>Cum sociis natoque penatibus et magnis dis parturient montes nascetur ridiculus mus In iaculis facilisis massa Etiam eu urna Sed porta Suspendisse quam leo molestie sed luctus quis feugiat in pede Fusce</p>
  <span class="more">READ MORE</span>
</article>
<article class="article" style="left:110px;top:884px">
  <div class="article-photo" role="img" aria-label="Photo of students kneeling in a row on blue mats" style="background:linear-gradient(180deg,#3f5f9a,#d8dde6 55%,#3b8fd0)"></div>
  <h3>Kihon Training</h3>
  <p>Cum sociis natoque penatibus et magnis dis parturient montes nascetur ridiculus mus In iaculis facilisis massa Etiam eu urna Sed porta Suspendisse quam leo molestie sed luctus quis feugiat in pede Fusce</p>
  <span class="more">READ MORE</span>
</article>
<article class="article" style="left:505px;top:884px">
  <div class="article-photo" role="img" aria-label="Photo of a karateka in a white gi practising outdoors" style="background:linear-gradient(135deg,#8a7a55,#e6e2d8 45%,#7f9a4a)"></div>
  <h3>Goshin Jitsu</h3>
  <p>Cum sociis natoque penatibus et magnis dis parturient montes nascetur ridiculus mus In iaculis facilisis massa Etiam eu urna Sed porta Suspendisse quam leo molestie sed luctus quis feugiat in pede Fusce</p>
  <span class="more">READ MORE</span>
</article>

<footer class="footer">
  <ul class="footer-col" style="left:110px">
    <li>Home</li><li>About Us</li><li>Location &amp; Times</li><li>News&nbsp; Events</li>
  </ul>
  <ul class="footer-col" style="left:251px">
    <li>Gallery &amp; Videos</li><li>Get Started</li><li>Contact Us</li>
  </ul>
  <div class="footer-contact">
    <h4>Contact Us</h4>
    <div class="addr">48 Harlow Lane #3 Brindale 20417</div>
    <div class="phone">555.010.2238</div>
    <div class="mail">info@sorvanedojo.example</div>
  </div>
  <div class="footer-brand"><span class="brand-mark"></span><span class="brand-name">Sorvane Dojo Karate</span></div>
</footer>
<div class="bottom-bar">
  <div class="copyright">© 2015 Company Name&nbsp; All right reserved&nbsp; Term of Use</div>
</div>
</body>
</html>
```